Investor Information Presentation Design Required and Corporate overview design

I have all the materials ready to go, just need 1x Pro Design for the presentation and 1x Pro Design for the corporate overview.
I am ok with images being changed (only if it represents the company better). Wording Can NOT be changed. Any process diagrams can be changed to better represent the process.
I can provide high res Logo file and obviously the files for the presentation and corporate overview. What I have done is basic, but need it to look far more polished and professional.

Target Market(s)

Fixed Term Deposits - $100,000 + High interest rates

Industry/Entity Type

Investment

Font styles to use
Sans Serif

Requirements
Must have
• A corporate professional look, think banks, financial services, business etc
• The presentation is NOT used for group presenting purposes - Individuals go through it on their own. Should want to make me feel like I have to read it all!

```html
<!DOCTYPE html>
<html lang="en">
<head>
<meta charset="utf-8">
<title>Experienced Senior Management – Northbay Capital</title>
<link rel="stylesheet" href="https://fonts.googleapis.com/css2?family=Arimo:wght@700&family=Open+Sans:wght@400;600;700&display=swap">
<style>
  :root{
    --title-blue:#29a3e0;
    --name-blue:#0d58a0;
    --role-blue:#2ea2dc;
    --text-grey:#444a50;
    --band-top:#1f93d8;
    --band-bottom:#3aa9e8;
    --header-light:#c3e9ef;
    --header-fade:#eaf7fa;
    --panel:#ececee;
    --logo-navy:#1f2a66;
    --photo-a:#b9bcc0;
    --photo-b:#5d6166;
  }
  *{margin:0;padding:0;box-sizing:border-box}
  html,body{width:1001px;height:1200px;overflow:hidden;background:#fff}
  body{position:relative;font-family:"Open Sans",Arial,sans-serif}
  .slide{position:absolute;left:0;width:1001px;height:566px;overflow:hidden;
    background:radial-gradient(ellipse 420px 300px at 760px 220px,#fafafa 0%,var(--panel) 100%)}
  .slide--one{top:0}
  .slide--two{top:634px}
  .header-band{position:absolute;left:0;top:0;width:1001px;height:128px;
    background:linear-gradient(90deg,var(--header-fade) 0%,var(--header-light) 45%,#d7f0f4 75%,#f3fafb 100%)}
  .slide-title{position:absolute;left:80px;top:42px;font-family:"Arimo",Arial,sans-serif;
    font-weight:700;font-size:37px;color:var(--title-blue);letter-spacing:-.2px}
  .brand-badge{position:absolute;left:836px;top:8px;width:158px;height:158px;border-radius:50%;
    background:radial-gradient(circle at 50% 45%,#ffffff 0%,#dff3f7 70%,#c7eaf1 100%);
    border:7px solid #fff;display:flex;align-items:center;justify-content:center}
  .brand-name{font-family:"Open Sans",Arial,sans-serif;font-weight:600;font-size:15px;
    color:var(--logo-navy);letter-spacing:.8px;margin-top:40px}
  .footer-band{position:absolute;left:0;top:470px;width:1001px;height:96px;
    background:linear-gradient(180deg,var(--band-top) 0%,var(--band-bottom) 100%);
    color:#fff;font-size:15px}
  .contact{position:absolute;top:40px;display:flex;align-items:center;gap:6px}
  .contact--email{left:29px}
  .contact--web{right:36px}
  .member{position:absolute;top:147px;width:250px}
  .portrait{display:block;width:150px;height:150px;margin:0 auto;border-radius:50%;
    border:7px solid #fff;background:radial-gradient(circle at 50% 40%,var(--photo-a) 0%,var(--photo-b) 100%)}
  .member-name{margin-top:9px;text-align:center;font-weight:700;font-size:12.5px;color:var(--name-blue)}
  .member-role{margin-top:1px;text-align:center;font-size:13px;color:var(--role-blue);
    display:flex;justify-content:center;align-items:center;gap:8px}
  .social-square{width:17px;height:17px;background:var(--name-blue);display:inline-block}
  .member-points{margin-top:8px;list-style:none;font-size:10.4px;line-height:1.12;color:var(--text-grey)}
  .member-points li{position:relative;padding-left:13px;margin-bottom:6px}
  .member-points li::before{content:"";position:absolute;left:1px;top:5px;width:3.5px;height:3.5px;border-radius:50%;background:var(--text-grey)}
  .slide--one .member-points{padding-left:20px}
  .slide--two .member{width:240px}
  .slide--two .member-points{padding-left:9px}
</style>
</head>
<body>

<section class="slide slide--one">
  <div class="header-band"></div>
  <h1 class="slide-title">Experienced Senior Management</h1>
  <div class="brand-badge"><span class="brand-name">Northbay Capital</span></div>

  <div class="member" style="left:124px">
    <div class="portrait" role="img" aria-label="Portrait photo of Daniel Ashcroft"></div>
    <p class="member-name">DANIEL ASHCROFT</p>
    <p class="member-role">Managing Director <span class="social-square"></span></p>
    <ul class="member-points">
      <li>Former CEO &amp; Managing Director of AXE-listed company</li>
      <li>Extensive international investment experience</li>
      <li>Bachelor of Laws, Bachelor of Commerce (Investment Finance Major)</li>
      <li>Winner 2013 40 Under 40 Award</li>
      <li>Founder of The Float Launch Co.</li>
    </ul>
  </div>

  <div class="member" style="left:375px">
    <div class="portrait" role="img" aria-label="Portrait photo of Rafiq Haddad"></div>
    <p class="member-name">RAFIQ HADDAD</p>
    <p class="member-role">Managing Partner <span class="social-square"></span></p>
    <ul class="member-points">
      <li>Former business owner &amp; operator</li>
      <li>Manages day-to-day operations relating to investors</li>
      <li>Specialists in digital strategies for business operations</li>
      <li>BSc Psychology - B. Eng. Bio-Medical Engineering and Applied Physics</li>
    </ul>
  </div>

  <div class="member" style="left:626px">
    <div class="portrait" role="img" aria-label="Portrait photo of Omar Latif"></div>
    <p class="member-name">OMAR LATIF</p>
    <p class="member-role">Senior Account Manager <span class="social-square"></span></p>
    <ul class="member-points">
      <li>10+ years financial services experience</li>
      <li>Former Stockbroker for leading Australian broking firm</li>
      <li>Works with new and existing investors</li>
      <li>Sourcing new investment opportunities</li>
    </ul>
  </div>

  <div class="footer-band">
    <span class="contact contact--email">
      <svg width="16" height="12" viewBox="0 0 16 12" aria-hidden="true"><rect x="0.75" y="0.75" width="14.5" height="10.5" fill="none" stroke="#fff" stroke-width="1.3"/><path d="M1 1l7 6 7-6M1 11l5-4.5M15 11l-5-4.5" fill="none" stroke="#fff" stroke-width="1.1"/></svg>
      info@northbaycapital.com.au</span>
    <span class="contact contact--web">
      <svg width="14" height="14" viewBox="0 0 14 14" aria-hidden="true"><g fill="none" stroke="#fff" stroke-width="1.1"><circle cx="7" cy="7" r="6.2"/><ellipse cx="7" cy="7" rx="2.8" ry="6.2"/><path d="M0.8 7h12.4M2 3.6h10M2 10.4h10"/></g></svg>
      www.northbaycapital.com.au</span>
  </div>
</section>

<section class="slide slide--two">
  <div class="header-band"></div>
  <h1 class="slide-title">Experienced Senior Management</h1>
  <div class="brand-badge"><span class="brand-name">Northbay Capital</span></div>

  <div class="member" style="left:3px">
    <div class="portrait" role="img" aria-label="Portrait photo of Nikos Daralis"></div>
    <p class="member-name">NIKOS DARALIS</p>
    <p class="member-role">Senior Account Manager <span class="social-square"></span></p>
    <ul class="member-points">
      <li>Financial Conduct Board (FCB) regulated professional</li>
      <li>Former Stockbroker &amp; Head of Equity Derivatives</li>
      <li>Works with new and existing investors</li>
      <li>Sources new investment opportunities</li>
    </ul>
  </div>

  <div class="member" style="left:254px">
    <div class="portrait" role="img" aria-label="Photo of Graham Felton seated"></div>
    <p class="member-name">GRAHAM FELTON</p>
    <p class="member-role">Senior Advisor &amp; UK Representative <span class="social-square"></span></p>
    <ul class="member-points">
      <li>Founder of Continental Wireline PLC (listed on LXE in 1996)</li>
      <li>Specialist in management consulting, due diligence &amp; stock market listings in London</li>
      <li>Provides Pre-vetted investment opportunities</li>
    </ul>
  </div>

  <div class="member" style="left:506px">
    <div class="portrait" role="img" aria-label="Portrait photo of Neil Whitford"></div>
    <p class="member-name">NEIL WHITFORD</p>
    <p class="member-role">General Counsel <span class="social-square"></span></p>
    <ul class="member-points">
      <li>20+ years’ experience in commercial law in private practice</li>
      <li>10 years’ experience as company secretary and in-house counsel</li>
      <li>Advises on compliance and legal requirements</li>
    </ul>
  </div>

  <div class="member" style="left:757px">
    <div class="portrait" role="img" aria-label="Portrait photo of Lina Hartono"></div>
    <p class="member-name">LINA HARTONO</p>
    <p class="member-role">Finance Manager <span class="social-square"></span></p>
    <ul class="member-points">
      <li>CPA Qualified Accountant</li>
      <li>Ledgra Certified Advisor</li>
      <li>Manages’ Northbay Capital’s finances</li>
    </ul>
  </div>

  <div class="footer-band">
    <span class="contact contact--email">
      <svg width="16" height="12" viewBox="0 0 16 12" aria-hidden="true"><rect x="0.75" y="0.75" width="14.5" height="10.5" fill="none" stroke="#fff" stroke-width="1.3"/><path d="M1 1l7 6 7-6M1 11l5-4.5M15 11l-5-4.5" fill="none" stroke="#fff" stroke-width="1.1"/></svg>
      info@northbaycapital.com.au</span>
    <span class="contact contact--web">
      <svg width="14" height="14" viewBox="0 0 14 14" aria-hidden="true"><g fill="none" stroke="#fff" stroke-width="1.1"><circle cx="7" cy="7" r="6.2"/><ellipse cx="7" cy="7" rx="2.8" ry="6.2"/><path d="M0.8 7h12.4M2 3.6h10M2 10.4h10"/></g></svg>
      www.northbaycapital.com.au</span>
  </div>
</section>

</body>
</html>
```